English and Spanish Language School Needs a Business Card

Need a business card design a startup company called Corvella Language School. The company will offer English and Spanish conversational level courses designed to make the learner feel comfortable with grammar and vocabulary. We would like to see a logo with some colour that should communicate learning, growth.

Target Market(s)

Consumers and businesses

Industry/Entity Type

Education

Contact Information for Business Card

TBD

Font styles to use
Serif

Requirements
Must have
• Include the following
• Logo
• Name
• Title
• Cellphone Number
• Office Phone number
• Email address
• Office Address

```html
<!DOCTYPE html>
<html lang="it">
<head>
<meta charset="utf-8">
<title>Corvella Language School – Business Card</title>
<link rel="stylesheet" href="https://fonts.googleapis.com/css2?family=Arimo:wght@400;700&display=swap">
<style>
  :root {
    --canvas: #ffffff;
    --card: #ffffff;
    --card-edge: #c9c9c9;
    --brand-red: #c0202a;
    --brand-teal: #14a2a4;
    --soft-teal: #9fd0d2;
    --soft-rose: #e0939a;
    --deep-slate: #5a5560;
    --ink: #1a1a1a;
  }
  html, body {
    margin: 0;
    width: 1200px;
    height: 1200px;
    overflow: hidden;
    background: var(--canvas);
  }
  .sheet {
    position: relative;
    width: 1200px;
    height: 1200px;
    font-family: "Arimo", Arial, sans-serif;
    color: var(--ink);
  }
  .card {
    position: absolute;
    width: 482px;
    background: var(--card);
    border: 1.5px solid var(--card-edge);
    box-sizing: border-box;
    overflow: hidden;
  }
  .card--front { left: 98px; top: 436px; height: 318px; }
  .card--back  { left: 620px; top: 448px; height: 314px; }

  .swoosh {
    position: absolute;
    left: 0;
    top: 0;
    width: 100%;
    height: 100%;
  }

  .brand {
    position: absolute;
    color: var(--brand-red);
    font-weight: 700;
    line-height: 1;
    white-space: nowrap;
  }
  .brand__name { display: block; letter-spacing: -1px; }
  .brand__tagline { display: block; }

  .card--front .brand { left: 38px; top: 64px; }
  .card--front .brand__name { font-size: 68px; }
  .card--front .brand__tagline { font-size: 19px; margin: 6px 0 0 26px; }

  .card--back .brand { left: 30px; top: 42px; }
  .card--back .brand__name { font-size: 32px; letter-spacing: -0.5px; }
  .card--back .brand__tagline { font-size: 10px; margin: 3px 0 0 6px; }

  .person {
    position: absolute;
    left: 178px;
    top: 136px;
    white-space: nowrap;
  }
  .person__name { font-size: 24px; }
  .person__title { font-size: 16px; margin-left: 8px; }

  .contact {
    position: absolute;
    left: 0;
    top: 190px;
    width: 100%;
    font-size: 16px;
    line-height: 24px;
  }
  .contact__row { display: flex; }
  .contact__label { width: 244px; text-align: right; }
  .contact__value { margin-left: 8px; }
</style>
</head>
<body>
<main class="sheet">

  <section class="card card--front" aria-label="Fronte del biglietto">
    <svg class="swoosh" viewBox="0 0 482 318" preserveAspectRatio="none" aria-hidden="true">
      <defs>
        <linearGradient id="front-wave" x1="0" y1="0" x2="1" y2="0">
          <stop offset="0" stop-color="var(--brand-teal)"/>
          <stop offset="0.45" stop-color="var(--deep-slate)"/>
          <stop offset="1" stop-color="var(--brand-red)"/>
        </linearGradient>
      </defs>
      <path d="M0,318 Q210,178 482,184 L482,318 Z" fill="url(#front-wave)"/>
    </svg>
    <div class="brand">
      <span class="brand__name">Corvella</span>
      <span class="brand__tagline">Language School</span>
    </div>
  </section>

  <section class="card card--back" aria-label="Retro del biglietto">
    <svg class="swoosh" viewBox="0 0 482 314" preserveAspectRatio="none" aria-hidden="true">
      <defs>
        <linearGradient id="back-top" x1="0" y1="0" x2="1" y2="0">
          <stop offset="0" stop-color="var(--soft-teal)"/>
          <stop offset="1" stop-color="var(--soft-rose)"/>
        </linearGradient>
        <linearGradient id="back-bottom" x1="0" y1="0" x2="1" y2="0">
          <stop offset="0" stop-color="var(--soft-rose)"/>
          <stop offset="1" stop-color="var(--soft-teal)"/>
        </linearGradient>
      </defs>
      <path d="M0,0 Q200,72 482,78 L482,0 Z" fill="url(#back-top)"/>
      <path d="M0,234 Q300,230 482,314 L0,314 Z" fill="url(#back-bottom)"/>
    </svg>
    <div class="brand">
      <span class="brand__name">Corvella</span>
      <span class="brand__tagline">Language School</span>
    </div>
    <div class="person">
      <span class="person__name">Nome</span><span class="person__title">Titolo</span>
    </div>
    <div class="contact">
      <div class="contact__row">
        <span class="contact__label">numero di cellulare</span>
        <span class="contact__value">N. Office Phone</span>
      </div>
      <div class="contact__row">
        <span class="contact__label">Indirizzo e-mail</span>
        <span class="contact__value">sito Indirizzo</span>
      </div>
    </div>
  </section>

</main>
</body>
</html>
```